Start up in business consultancy needs a business card

We need the business card's layout (we have already the logo). Our business is concerned on consultancy services delivered to companies on the matter of sustainability. Business card should be enough essentials and professional style.

Side A with the following info:
logo + a space for the claim (still to identify) + website of the company

Side B with the following info:
Name of business card holder + title of the business card holder + address of the company + space for mobile number, phone number, fax number + e-mail of business card holder + graphic details around.

Target Market(s)

Business of any sector

Industry/Entity Type

Business Service

Contact Information for Business Card

Name of the company:
Pianoverde srl
Società Benefit

Address of the company:
Via Lucerna, 7
21047 - Saronno (VA)

Website:
www.pianoverde.it

Name of the BC' holder:
Luca Ferentino

Title:
Co-fondatore

Email:
luca@pianoverde.it

Mobile:
+39 348 915 2074
Phone:
+39 348 915 2074
Fax:
+39 348 915 2074

Font styles to use
Other font styles liked:
• new gothic

```html
<!DOCTYPE html>
<html lang="it">
<head>
<meta charset="utf-8">
<title>Pianoverde – Biglietto da visita</title>
<link rel="stylesheet" href="https://fonts.googleapis.com/css2?family=Mulish:wght@700&family=Questrial&family=Source+Sans+3:wght@400;600;700&display=swap">
<style>
  :root {
    --brand-blue: #0868ad;
    --text-grey: #4a4a4a;
    --divider: #c9c9c9;
    --paper: #ffffff;
    --backdrop: #e8e5e1;
  }
  * { margin: 0; padding: 0; box-sizing: border-box; }
  html, body {
    width: 1200px; height: 987px; overflow: hidden;
    background: var(--backdrop);
    font-family: "Source Sans 3", "Myriad Pro", Arial, sans-serif;
  }
  .canvas { position: relative; width: 1200px; height: 987px; }
  .card {
    position: absolute; left: 293px; width: 615px; height: 352px;
    box-shadow: 0 2px 6px rgba(0,0,0,.18);
  }
  .card--front { top: 130px; background: var(--paper); }
  .card--back { top: 506px; background: var(--brand-blue); }

  .brand { position: absolute; display: flex; align-items: center; }
  .brand__dot {
    border-radius: 50%; border: 4px solid var(--brand-blue); flex: none;
  }
  .brand__name { color: var(--brand-blue); font-weight: 600; }
  .card--front .brand { left: 66px; top: 137px; gap: 12px; }
  .card--front .brand__dot { width: 72px; height: 72px; }
  .card--front .brand__name { font-size: 27px; letter-spacing: -0.2px; }

  .divider {
    position: absolute; left: 328px; top: 52px; width: 1px; height: 254px;
    background: var(--divider);
  }
  .details { position: absolute; left: 353px; top: 50px; color: var(--text-grey); }
  .holder__name {
    font-family: "Mulish", "Century Gothic", sans-serif; font-weight: 700;
    font-size: 23px; color: var(--brand-blue); line-height: 28px;
  }
  .holder__title {
    font-family: "Questrial", "Century Gothic", sans-serif;
    font-size: 17px; color: var(--text-grey); line-height: 20px; margin-left: -2px;
  }
  .company { margin-top: 11px; font-size: 16px; line-height: 22px; }
  .company__name { font-weight: 700; }
  .contacts { list-style: none; margin-top: 13px; font-size: 16px; }
  .contacts li { display: flex; align-items: center; gap: 8px; height: 23.5px; }
  .contacts svg { width: 16px; height: 16px; fill: var(--brand-blue); flex: none; }

  .card--back .brand {
    left: 0; right: 0; top: 121px; justify-content: center; gap: 16px;
  }
  .card--back .brand__dot { width: 80px; height: 80px; border: 5px solid var(--paper); }
  .card--back .brand__name { color: var(--paper); font-size: 40px; }
  .website {
    position: absolute; left: 0; right: 0; top: 291px; text-align: center;
    color: var(--paper); font-size: 16px; letter-spacing: 3.2px;
  }
</style>
</head>
<body>
<main class="canvas">
  <section class="card card--front">
    <div class="brand">
      <span class="brand__dot"></span>
      <span class="brand__name">pianoverde</span>
    </div>
    <div class="divider"></div>
    <div class="details">
      <h1 class="holder__name">Luca Ferentino</h1>
      <p class="holder__title">Co-fondatore</p>
      <address class="company" style="font-style:normal">
        <div class="company__name">Pianoverde srl</div>
        <div>Società Benefit</div>
        <div>Via Lucerna, 7</div>
        <div>21047 - Saronno (VA)</div>
      </address>
      <ul class="contacts">
        <li><svg viewBox="0 0 16 16" aria-hidden="true"><path d="M3.5 1.5l2.3 2.6-1.2 1.8c.9 2 2.4 3.6 4.5 4.6l1.8-1.2 2.6 2.3-1.3 2.2C7 13.4 2.6 9 1.3 3z"/></svg>+39 348 915 2074</li>
        <li><svg viewBox="0 0 16 16" aria-hidden="true"><path d="M4.5 1h7v14h-7zM6 2.6v9.4h4V2.6z"/></svg>+39 348 915 2074</li>
        <li><svg viewBox="0 0 16 16" aria-hidden="true"><path d="M4 1h8v4H4zM1 6h14v6H1zM3 13h10v2H3z"/></svg>+39 348 915 2074</li>
        <li><svg viewBox="0 0 16 16" aria-hidden="true"><path d="M1 3.5h14v9H1zM2.5 4.5L8 8.7l5.5-4.2v1.3L8 10 2.5 5.8z"/></svg>luca@pianoverde.it</li>
      </ul>
    </div>
  </section>

  <section class="card card--back">
    <div class="brand">
      <span class="brand__dot"></span>
      <span class="brand__name">pianoverde</span>
    </div>
    <p class="website">www.pianoverde.it</p>
  </section>
</main>
</body>
</html>
```